Business Card For Video Production Company

Please NOTE: I've added some info to the must haves that I should have included at the start. Thank you.

I need a business card design for my video production company based in Orlando called Caldera Film Works. Our work consists of web video marketing (web videos), training videos, sales videos, conference and seminar video production...basically a lot of corporate based work.

We work with successful small businesses, not-for-profits and some Fortune 500 type groups. We bring a lot of knowledge, experience and attention to detail to every project.

I'd like something that communicates strength, confidence, integrity, as well as creative vision. I want to stay away from the standard icons of the media and film industry. I'd like to emphasize the colors of my logo, and also the colors of my website which has a white background. Simple is good.

Our budgets are moderate...generally $1500 to $5000.

www.calderafilm.tv

PS...We don't do weddings or recitals, or that type of production.
Updates

I want to thank all the designers for your updates. There's way too many to be able to give feedback on for all. I hope you understand that. But wow…there are so many great designs everyone has offered. I can't thank you enough…each and everyone. I hope to make my decision soon. I'm not accepting anymore designs from new designers. Brent-

Target Market(s)

Successful small businesses, marketing directors, corporate communication directors, training and human resources professionals. forward thinking not-for profits. Since my company is based in Central Florida, most of my work comes from this area too.

Industry/Entity Type

Marketing

Requirements
Must have
• website address, www.calderafilm.tv
phone number, 407-552-9031
email address, brent@calderafilm.tv

Title
Brent Caldera
Owner/Creative Director

I'd like to have a single line that goes across illustrating our services, maybe separated with bullet points:

Marketing Videos, Corporate Videos, Conference & Seminar Video Production
Should not have
• No film or video icons.
No need to pull language or copy from my website.

```html
<!DOCTYPE html>
<html lang="en">
<head>
<meta charset="utf-8">
<title>Caldera Film Works – Business Card</title>
<link rel="stylesheet" href="https://fonts.googleapis.com/css2?family=Montserrat:wght@400;700&family=Oswald:wght@500&family=Open+Sans:wght@400;600&display=swap">
<style>
  :root {
    --brand-blue: #2b8fd0;
    --brand-blue-deep: #1f7bbd;
    --brand-blue-light: #39a3dd;
    --paper: #f3f3f1;
    --ink: #3a3a3a;
    --ink-soft: #6d6d6d;
    --icon-grey: #6a6a6a;
    --stage: #e4e6e8;
  }
  * { box-sizing: border-box; margin: 0; padding: 0; }
  html, body { width: 1200px; height: 873px; overflow: hidden; }
  body {
    background: var(--stage);
    display: flex; align-items: center; justify-content: center; gap: 40px;
    font-family: "Open Sans", sans-serif;
  }
  .card {
    position: relative; width: 540px; height: 308px; overflow: hidden;
    box-shadow: 0 6px 18px rgba(0,0,0,.18);
  }

  /* Front */
  .card--front { background: var(--paper); }
  .front__top-rule { position: absolute; left: 0; top: 0; width: 100%; height: 8px; background: var(--brand-blue); }
  .front__services {
    position: absolute; left: 0; bottom: 0; width: 100%; height: 34px;
    background: var(--brand-blue); color: #fff;
    display: flex; align-items: center; justify-content: center;
    font-size: 10.5px; letter-spacing: 1.6px;
  }
  .front__bar-h { position: absolute; left: 232px; top: 124px; width: 308px; height: 22px; background: var(--brand-blue); }
  .front__bar-v { position: absolute; left: 232px; top: 124px; width: 22px; height: 150px; background: var(--brand-blue); }
  .holder { position: absolute; left: 34px; top: 62px; width: 190px; text-align: right; }
  .holder__name { font-family: "Oswald", sans-serif; font-weight: 500; font-size: 22px; letter-spacing: .5px; color: var(--ink); }
  .holder__title { font-size: 10px; color: var(--ink-soft); margin-top: 2px; }
  .brand-line {
    position: absolute; right: 28px; top: 50px;
    display: flex; align-items: center; gap: 10px;
    font-family: "Montserrat", sans-serif; font-weight: 700; font-size: 21px; color: var(--ink);
  }
  .brand-line__mark { width: 22px; height: 22px; background: var(--brand-blue); }
  .contact { position: absolute; left: 224px; top: 162px; }
  .contact__row { display: flex; align-items: center; gap: 16px; height: 34px; }
  .contact__icon {
    width: 38px; height: 28px; border-radius: 6px; background: var(--icon-grey);
    display: flex; align-items: center; justify-content: center;
  }
  .contact__text { font-size: 12.5px; color: var(--ink); }

  /* Back */
  .card--back { background: linear-gradient(135deg, var(--brand-blue-light), var(--brand-blue-deep)); }
  .back__brand {
    position: absolute; left: 0; right: 0; top: 112px;
    display: flex; align-items: center; justify-content: center; gap: 14px;
    font-family: "Montserrat", sans-serif; font-weight: 700; font-size: 30px; color: #fff;
  }
  .back__brand-mark { width: 34px; height: 34px; background: #fff; }
  .back__services {
    position: absolute; left: 0; bottom: 0; width: 100%; height: 26px;
    background: var(--paper); color: var(--brand-blue-deep);
    display: flex; align-items: center; justify-content: center;
    font-size: 10px; font-weight: 600; letter-spacing: 1.4px;
  }
</style>
</head>
<body>
  <section class="card card--front" aria-label="Business card front">
    <div class="front__top-rule"></div>
    <div class="front__bar-h"></div>
    <div class="front__bar-v"></div>

    <div class="holder">
      <p class="holder__name">BRENT CALDERA</p>
      <p class="holder__title">Owner/Creative Director</p>
    </div>

    <div class="brand-line">
      <span class="brand-line__mark"></span>
      <span>Caldera Film Works</span>
    </div>

    <div class="contact">
      <div class="contact__row">
        <span class="contact__icon">
          <svg width="14" height="14" viewBox="0 0 24 24" fill="#fff"><path d="M6.6 10.8a15 15 0 0 0 6.6 6.6l2.2-2.2c.3-.3.7-.4 1-.2 1.1.4 2.3.6 3.6.6.6 0 1 .4 1 1V20c0 .6-.4 1-1 1A17 17 0 0 1 3 4c0-.6.4-1 1-1h3.5c.6 0 1 .4 1 1 0 1.3.2 2.5.6 3.6.1.3 0 .7-.2 1z"/></svg>
        </span>
        <span class="contact__text">407-552-9031</span>
      </div>
      <div class="contact__row">
        <span class="contact__icon">
          <svg width="16" height="12" viewBox="0 0 24 18" fill="none" stroke="#fff" stroke-width="2"><rect x="1" y="1" width="22" height="16" rx="1"/><path d="M1 2l11 8 11-8"/></svg>
        </span>
        <span class="contact__text">brent@calderafilm.tv</span>
      </div>
      <div class="contact__row">
        <span class="contact__icon">
          <svg width="14" height="14" viewBox="0 0 24 24" fill="none" stroke="#fff" stroke-width="2"><circle cx="12" cy="12" r="10"/><path d="M2 12h20M12 2c3 3 3 17 0 20M12 2c-3 3-3 17 0 20"/></svg>
        </span>
        <span class="contact__text">www.calderafilm.tv</span>
      </div>
    </div>

    <p class="front__services">Marketing Videos, Corporate Videos, Conference &amp; Seminar Video Production</p>
  </section>

  <section class="card card--back" aria-label="Business card back">
    <div class="back__brand">
      <span class="back__brand-mark"></span>
      <span>Caldera Film Works</span>
    </div>
    <p class="back__services">Marketing Videos, Corporate Videos, Conference &amp; Seminar Video Production</p>
  </section>
</body>
</html>
```